IT Services company requires a services website design with integrated blog

We at Brindle Harbour Systems primarily provide application migration consultancy (e.g. moving applications from Plexor OS 4 to Plexor 9) and application virtualization (e.g. Norvane StackPod) consultancy.This process is commonly known as 'packaging' but doesnt involve cardboard boxes ;) (however, I am happy to use that visual analogy if you want to use any box graphics) We also provide application compatibility testing, software auditing and application portfolio management.

We are looking for a complete redesign of our current horrible diy attempt at a website at www.example-vendorhub.test. We have had created a rebranded logo (attached files and fonts) and a rebranded business card (also attached) We would like the website to match the same/similar colors and styling as these.

I want to redisgn the website so that the main focus of this website is to show our subject matter expertise with a blog and should take up most of the websites real estate and focus on the home screen. Then if the customer wants, they can use our services to help them in their own application migration/deployment projects by browsing our details in links/buttons somewhere
Updates

In any of the designs, please do not include my Quellbright or Norvane partnerships.  Thank you

Target Market(s)

Application packagers / engineers looking for technical articles

Application migration project managers

Industry/Entity Type

Real Estate

Requirements
Must have
• This site is primarily a blog site. The blog should have buttons to share each article on social media site. It should be easy for me to create or edit new blog articles (have technical skills but not creative ones). Each article should also allow for comments (do not require approval but should allow for admin removal) but do not add like/vote buttons because i do not expect large enough traffic and could be determental.

There should be a contact page to host contact information and an email box that goes to enquiries@example-vendorhub.test

The other pages should include About us and Services (placeholder text to be used as current site text needs overhauling but original text can be used in the design just remember when placing that the text may shorten or increase etc.)

All text has to be easily editable (no over use of text in images where possible)
Nice to have
• An email notification of new comments to articles sent to webadmin@example-vendorhub.test

Newsletter subscription
Should not have
• Do not include vote/like buttons or website counters. Initial traffic is not going to be large enough to warrant these features and may reflect badly on the site.

No logon features. Site content and commenting should be open access

No opinion polls

No why choose us section from current website

Do not include partner information in new site (Quellbright and Norvane)

DO NOT JUST REPLICATE EXISTING WEBSITE FEATURES, PLEASE REFER TO THIS BRIEF. THIS SITE NEEDS TO PRIMARILY BE A BLOG

```html
<!DOCTYPE html>
<html lang="en">
<head>
<meta charset="utf-8">
<title>Brindle Harbour Systems – Blog</title>
<link rel="stylesheet" href="https://fonts.googleapis.com/css2?family=Arimo:ital,wght@0,400;0,700;1,400&display=swap">
<style>
:root{
  --brand-blue:#6b84da;
  --link-blue:#3f63d6;
  --ink:#2b2b2b;
  --body-text:#5a5a5a;
  --muted:#8a8a8a;
  --taupe:#6b665a;
  --panel:#f0f1f5;
  --panel-head:#e2e3e8;
  --rule:#dcdcdc;
  --white:#ffffff;
  --navy:#1f2f7a;
}
*{box-sizing:border-box;margin:0;padding:0}
html,body{width:1200px;height:998px;overflow:hidden;background:var(--white)}
body{font-family:"Arimo",Arial,sans-serif;color:var(--ink);position:relative}
a{text-decoration:none;color:inherit}

/* top navigation */
.topbar{position:absolute;left:0;top:0;width:1200px;height:28px;background:var(--brand-blue);border-bottom:2px solid #2c2f3a}
.topbar__nav{position:absolute;left:200px;top:0;display:flex;height:26px;align-items:center}
.topbar__nav a{color:var(--white);font-size:10px;padding:0 18px;border-left:1px dotted rgba(255,255,255,.45)}
.topbar__nav a:first-child{padding-left:0;border-left:0}
.topbar__social{position:absolute;right:200px;top:5px;display:flex;gap:6px}
.topbar__social span{width:16px;height:16px;border-radius:50%;background:var(--white)}

/* header */
.brand{position:absolute;left:200px;top:54px;display:flex;align-items:center;gap:10px}
.brand__mark{width:44px;height:44px;border-radius:50%;background:var(--brand-blue)}
.brand__name{font-size:20px;color:var(--taupe);line-height:1.05;width:160px}
.quote{position:absolute;left:470px;top:45px;width:530px;height:67px;background:var(--taupe);color:#e9e7e1;padding:6px 12px}
.quote__text{font-size:20px;font-weight:400;line-height:25px;letter-spacing:-.5px}
.quote__source{position:absolute;right:12px;bottom:11px;font-size:15px;font-style:normal;color:var(--white);letter-spacing:-.3px}
.header-rule{position:absolute;left:200px;top:132px;width:800px;height:1px;background:var(--rule)}

/* blog posts */
.posts{position:absolute;left:199px;top:146px;width:530px}
.post{position:relative;height:207px}
.post__title{font-size:24px;font-weight:400;color:var(--ink);line-height:28px}
.post__meta{position:absolute;top:33px;font-size:9.5px;font-style:italic;color:var(--muted)}
.post__meta a{color:var(--link-blue)}
.post__image{position:absolute;left:0;top:52px;width:146px;height:103px;border:2px solid #fff;box-shadow:0 0 3px rgba(0,0,0,.3)}
.post__image--keys{background:linear-gradient(135deg,#2c3550,#6e7aa8 55%,#c9cfe6)}
.post__image--laptop{background:linear-gradient(135deg,#f3f3f3,#c8d4e6 55%,#e8a640)}
.post__image--globe{background:radial-gradient(circle at 45% 35%,#5f8fd8,#c9d8ef 45%,#ffffff 70%)}
.post__excerpt{position:absolute;left:163px;top:51px;width:370px;font-size:11.2px;line-height:17.6px;color:var(--body-text);letter-spacing:-.1px}
.post__more{position:absolute;left:163px;top:160px;font-size:11.6px;color:var(--link-blue)}
.share{position:absolute;left:336px;top:162px;display:flex;gap:7px}
.share__btn{display:flex;align-items:center;gap:6px;height:19px;padding:0 6px 0 2px;background:linear-gradient(#3a3a3a,#151515);border-radius:2px;box-shadow:0 1px 2px rgba(0,0,0,.4);color:var(--white);font-size:6.5px;width:59px}
.share__btn i{width:15px;height:15px;display:block}
.share__btn--a i{background:#3b5a9a}
.share__btn--b i{background:#2b9fd8}
.share__btn--c i{background:#f07c1a}
.post__rule{position:absolute;left:50px;top:194px;width:420px;height:1px;background:linear-gradient(90deg,transparent,#cfcfcf,transparent)}

/* pagination */
.pager{position:absolute;left:201px;top:792px;display:flex;gap:9px;align-items:center}
.pager span{width:21px;height:21px;border-radius:50%;background:var(--taupe);color:var(--white);font-size:13px;font-weight:700;display:flex;align-items:center;justify-content:center}
.pager .is-current{background:var(--brand-blue)}
.pager .pager__next{margin-left:20px;width:26px;height:26px;background:var(--brand-blue)}

.column-rule{position:absolute;left:744px;top:149px;width:1px;height:666px;background:var(--rule)}

/* sidebar */
.search{position:absolute;left:760px;top:149px;display:flex;gap:7px}
.search__input{width:162px;height:32px;border:1px solid #d4d4d4;font-size:9px;font-style:italic;color:#b4b4b4;padding:10px 8px}
.search__btn{width:70px;height:32px;background:var(--taupe);color:var(--white);font-size:12px;display:flex;align-items:center;justify-content:center}

.news{position:absolute;left:760px;top:221px;width:240px;height:595px;background:var(--panel);border-top:4px solid var(--brand-blue)}
.news__title{font-size:21px;color:var(--brand-blue);font-weight:400;padding:9px 10px 10px;border-bottom:1px solid #d4d5da;margin-bottom:16px}
.news__item{border-bottom:1px solid #c9cad0;margin-bottom:16px;padding-bottom:7px}
.news__item:last-of-type{border-bottom:0;margin-bottom:0}
.news__head{background:var(--panel-head);font-size:14px;font-weight:400;color:#3a3a3a;padding:6px 11px 5px;line-height:15px}
.news__body{padding:5px 10px 0 11px;font-size:8.6px;line-height:12px;color:#7a7a7a;letter-spacing:.2px}
.news__foot{position:relative;padding:0 10px 0 11px;font-size:9px;color:var(--ink);line-height:15px;margin-top:2px}
.news__tools{position:absolute;right:10px;top:2px;display:flex;gap:4px}
.news__more{display:block;padding:0 11px;font-size:10px;line-height:14px;color:var(--link-blue)}
.news__all{position:absolute;left:11px;bottom:9px;background:#4a4840;color:var(--white);font-size:11px;padding:4px 10px}

/* footer */
.footer{position:absolute;left:0;top:833px;width:1200px;height:134px;background:var(--brand-blue)}
.footer__col{position:absolute;top:22px}
.footer__col h3{font-size:13.5px;font-weight:400;color:var(--navy);margin-bottom:15px}
.footer__col li{list-style:none;font-size:9.6px;color:var(--white);line-height:16px;display:flex;align-items:center;gap:8px}
.footer__col--nav{left:199px}
.footer__col--follow{left:299px}
.footer__col--follow li{line-height:20.5px;gap:10px}
.footer__col--follow li i{width:14px;height:14px;border-radius:50%;background:var(--white);display:block}
.footer__col--contact{left:392px}
.footer__col--contact svg{flex:none}
.footer__col--news{left:556px}
.subscribe{display:flex;gap:7px;margin-top:-1px}
.subscribe__input{width:162px;height:32px;background:var(--white);border:1px solid #d4d8ef;font-size:9px;font-style:italic;color:#a8a8a8;padding:10px 8px}
.subscribe__btn{width:79px;height:32px;background:var(--taupe);color:var(--white);font-size:12px;display:flex;align-items:center;justify-content:center}
.footer__brand{position:absolute;left:834px;top:37px;display:flex;align-items:center;gap:10px;opacity:.75}
.footer__brand span{width:40px;height:40px;border-radius:50%;background:var(--white)}
.footer__brand b{font-weight:400;font-size:20px;color:var(--white);line-height:1.05;width:140px}

.legal{position:absolute;left:0;top:967px;width:1200px;height:31px;background:var(--taupe);color:#eeece6;font-size:9.6px;text-align:center;line-height:31px}
</style>
</head>
<body>

<header>
  <div class="topbar">
    <nav class="topbar__nav">
      <a href="#">Home</a><a href="#">About Us</a><a href="#">Our Services</a><a href="#">Blog</a><a href="#">Contact</a>
    </nav>
    <div class="topbar__social" aria-label="Social links"><span></span><span></span><span></span></div>
  </div>

  <div class="brand">
    <span class="brand__mark"></span>
    <span class="brand__name">Brindle Harbour Systems</span>
  </div>

  <blockquote class="quote">
    <p class="quote__text">Logistics - The detailed Oraganization and implementation of a Complex Operation</p>
    <cite class="quote__source">Harwell Lexicon</cite>
  </blockquote>
  <div class="header-rule"></div>
</header>

<main class="posts">
  <article class="post">
    <h2 class="post__title">Lorem ipsum dolor sit amet.</h2>
    <p class="post__meta">Posted by: <a href="#">BRINDLE HARBOUR SYSTEMS</a> on May 31, 2013</p>
    <div class="post__image post__image--keys" role="img" aria-label="Close-up of a keyboard with a blue digital overlay"></div>
    <p class="post__excerpt">Lorem ipsum dolor sit amet, consectetur adipiscing elit. Vestibulum aliqua augue id justo vulputate in cursus velit gravida. Nullam sit amet lectus. Cras venenatis mollis neque at aliquam. Suspendisse at arcu vitae sem rhoncus faucibus eget sed odio. Etiam eget nisi justo, ac tristique ante. Nam interdum convallis ipsum, ut bibendum velit laoreet sit amet. Nulla semper fringilla nibh, placerat iaculis mi eleifend quis.</p>
    <a class="post__more" href="#">Read more...</a>
    <div class="share">
      <a class="share__btn share__btn--a" href="#"><i></i>Friendline</a>
      <a class="share__btn share__btn--b" href="#"><i></i>Chirpcast</a>
      <a class="share__btn share__btn--c" href="#"><i></i>Postwell</a>
    </div>
    <div class="post__rule"></div>
  </article>

  <article class="post">
    <h2 class="post__title">Lorem ipsum dolor sit amet.</h2>
    <p class="post__meta">Posted by: <a href="#">BRINDLE HARBOUR SYSTEMS</a> on May 31, 2013</p>
    <div class="post__image post__image--laptop" role="img" aria-label="Illustration of a figure loading data into a laptop"></div>
    <p class="post__excerpt">Lorem ipsum dolor sit amet, consectetur adipiscing elit. Vestibulum aliqua augue id justo vulputate in cursus velit gravida. Nullam sit amet lectus. Cras venenatis mollis neque at aliquam. Suspendisse at arcu vitae sem rhoncus faucibus eget sed odio. Etiam eget nisi justo, ac tristique ante. Nam interdum convallis ipsum, ut bibendum velit laoreet sit amet. Nulla semper fringilla nibh, placerat iaculis mi eleifend quis.</p>
    <a class="post__more" href="#">Read more...</a>
    <div class="share">
      <a class="share__btn share__btn--a" href="#"><i></i>Friendline</a>
      <a class="share__btn share__btn--b" href="#"><i></i>Chirpcast</a>
      <a class="share__btn share__btn--c" href="#"><i></i>Postwell</a>
    </div>
    <div class="post__rule"></div>
  </article>

  <article class="post">
    <h2 class="post__title">Lorem ipsum dolor sit amet.</h2>
    <p class="post__meta">Posted by: <a href="#">BRINDLE HARBOUR SYSTEMS</a> on May 31, 2013</p>
    <div class="post__image post__image--globe" role="img" aria-label="Globe connected to computer mice by cables"></div>
    <p class="post__excerpt">Lorem ipsum dolor sit amet, consectetur adipiscing elit. Vestibulum aliqua augue id justo vulputate in cursus velit gravida. Nullam sit amet lectus. Cras venenatis mollis neque at aliquam. Suspendisse at arcu vitae sem rhoncus faucibus eget sed odio. Etiam eget nisi justo, ac tristique ante. Nam interdum convallis ipsum, ut bibendum velit laoreet sit amet. Nulla semper fringilla nibh, placerat iaculis mi eleifend quis.</p>
    <a class="post__more" href="#">Read more...</a>
    <div class="share">
      <a class="share__btn share__btn--a" href="#"><i></i>Friendline</a>
      <a class="share__btn share__btn--b" href="#"><i></i>Chirpcast</a>
      <a class="share__btn share__btn--c" href="#"><i></i>Postwell</a>
    </div>
  </article>
</main>

<nav class="pager" aria-label="Pages">
  <span>1</span><span>2</span><span class="is-current">3</span><span>4</span><span>5</span><span>6</span><span>7</span>
  <span class="pager__next"><svg width="10" height="12" viewBox="0 0 10 12"><path d="M2 1l5 5-5 5" fill="none" stroke="#fff" stroke-width="2.6"/></svg></span>
</nav>

<div class="column-rule"></div>

<aside>
  <form class="search">
    <div class="search__input">Enter you keyword...</div>
    <div class="search__btn">Search</div>
  </form>

  <section class="news">
    <h2 class="news__title">Latest News</h2>

    <div class="news__item">
      <h3 class="news__head">Packaging Workshop Dates</h3>
      <p class="news__body">Our next hands-on application packaging workshops are now open for booking, covering testing and migration basics</p>
      <p class="news__foot">Tuesday, 19 June 2012 16:47
        <span class="news__tools">
          <svg width="12" height="11" viewBox="0 0 12 11"><rect x="1" y=".5" width="9" height="10" fill="#fff" stroke="#888"/><path d="M3 7l2-3 2 3" stroke="#aaa" fill="none"/></svg>
          <svg width="14" height="11" viewBox="0 0 14 11"><rect x="3" y="0" width="8" height="4" fill="#999"/><rect x="0" y="3" width="14" height="6" rx="1" fill="#555"/><rect x="3" y="7" width="8" height="4" fill="#ddd"/></svg>
          <svg width="16" height="11" viewBox="0 0 16 11"><rect x=".5" y=".5" width="15" height="10" fill="#555"/><path d="M1 1l7 5 7-5" stroke="#ddd" fill="none"/></svg>
        </span>
      </p>
      <a class="news__more" href="#">Read more...</a>
    </div>

    <div class="news__item">
      <h3 class="news__head">New Compatibility Service</h3>
      <p class="news__body">We now offer application compatibility testing so that you can plan your move to Plexor 9 with far fewer surprises</p>
      <p class="news__foot">Tuesday, 19 June 2012 16:47
        <span class="news__tools">
          <svg width="12" height="11" viewBox="0 0 12 11"><rect x="1" y=".5" width="9" height="10" fill="#fff" stroke="#888"/><path d="M3 7l2-3 2 3" stroke="#aaa" fill="none"/></svg>
          <svg width="14" height="11" viewBox="0 0 14 11"><rect x="3" y="0" width="8" height="4" fill="#999"/><rect x="0" y="3" width="14" height="6" rx="1" fill="#555"/><rect x="3" y="7" width="8" height="4" fill="#ddd"/></svg>
          <svg width="16" height="11" viewBox="0 0 16 11"><rect x=".5" y=".5" width="15" height="10" fill="#555"/><path d="M1 1l7 5 7-5" stroke="#ddd" fill="none"/></svg>
        </span>
      </p>
      <a class="news__more" href="#">Read more...</a>
    </div>

    <div class="news__item">
      <h3 class="news__head">Brindle Harbour Systems Officially Launches!</h3>
      <p class="news__body">After years of experience working within software logistics we have now officially launched. Why not contact us to find out what we can do for you!</p>
      <p class="news__foot">Tuesday, 19 June 2012 16:47
        <span class="news__tools">
          <svg width="12" height="11" viewBox="0 0 12 11"><rect x="1" y=".5" width="9" height="10" fill="#fff" stroke="#888"/><path d="M3 7l2-3 2 3" stroke="#aaa" fill="none"/></svg>
          <svg width="14" height="11" viewBox="0 0 14 11"><rect x="3" y="0" width="8" height="4" fill="#999"/><rect x="0" y="3" width="14" height="6" rx="1" fill="#555"/><rect x="3" y="7" width="8" height="4" fill="#ddd"/></svg>
          <svg width="16" height="11" viewBox="0 0 16 11"><rect x=".5" y=".5" width="15" height="10" fill="#555"/><path d="M1 1l7 5 7-5" stroke="#ddd" fill="none"/></svg>
        </span>
      </p>
      <a class="news__more" href="#">Read more...</a>
    </div>

    <div class="news__item">
      <h3 class="news__head">Lorem Ipsum Dolor</h3>
      <p class="news__body">Lorem ipsum dolor sit amet, consectetur adipiscing elit. Vestibulum aliqua augue id justo vulputate in cursus velit gravida.</p>
      <p class="news__foot">Tuesday, 19 June 2012 16:47
        <span class="news__tools">
          <svg width="12" height="11" viewBox="0 0 12 11"><rect x="1" y=".5" width="9" height="10" fill="#fff" stroke="#888"/><path d="M3 7l2-3 2 3" stroke="#aaa" fill="none"/></svg>
          <svg width="14" height="11" viewBox="0 0 14 11"><rect x="3" y="0" width="8" height="4" fill="#999"/><rect x="0" y="3" width="14" height="6" rx="1" fill="#555"/><rect x="3" y="7" width="8" height="4" fill="#ddd"/></svg>
          <svg width="16" height="11" viewBox="0 0 16 11"><rect x=".5" y=".5" width="15" height="10" fill="#555"/><path d="M1 1l7 5 7-5" stroke="#ddd" fill="none"/></svg>
        </span>
      </p>
      <a class="news__more" href="#">Read more...</a>
    </div>

    <a class="news__all" href="#">View all</a>
  </section>
</aside>

<footer class="footer">
  <div class="footer__col footer__col--nav">
    <h3>Navigation</h3>
    <ul><li>Home</li><li>About Us</li><li>Our Services</li><li>Blog</li><li>Contact</li></ul>
  </div>
  <div class="footer__col footer__col--follow">
    <h3>Follow Us</h3>
    <ul><li><i></i>Friendline</li><li><i></i>Chirpcast</li><li><i></i>Blog</li></ul>
  </div>
  <div class="footer__col footer__col--contact">
    <h3>Contact Us</h3>
    <ul>
      <li><svg width="8" height="10" viewBox="0 0 8 10"><path d="M2 0l2 2-1 2 2 3 1-1 2 2-2 2C3 9 0 5 0 2z" fill="#fff"/></svg>0800-555-0142</li>
      <li><svg width="8" height="10" viewBox="0 0 8 10"><rect width="8" height="10" fill="#fff"/><rect x="2" y="2" width="4" height="2" fill="#6b84da"/></svg>0800-555-0143</li>
      <li><svg width="9" height="7" viewBox="0 0 9 7"><rect width="9" height="7" fill="#fff"/><path d="M0 0l4.5 4L9 0" stroke="#6b84da" fill="none"/></svg>info@example-vendorhub.test</li>
    </ul>
  </div>
  <div class="footer__col footer__col--news">
    <h3>Get our Latest Updates</h3>
    <form class="subscribe">
      <div class="subscribe__input">Enter your Email....</div>
      <div class="subscribe__btn">Subscribe</div>
    </form>
  </div>
  <div class="footer__brand"><span></span><b>Brindle Harbour Systems</b></div>
</footer>

<div class="legal">© 2012–2013 Brindle Harbour Systems,&nbsp; Terms &amp; Conditions : Privacy Policy</div>

</body>
</html>
```